I need email signatures for my admin staff members
info:
Darina Qubrosi
Support Coordinator
Unit 4, 517 Wattlebrook Lane, Kemberly NSW 2893
Tel: 02 84427193 Mob: 0427596314
email: darina.qu@mivrotelhaven.com
www.mivrotelhaven.com

Target Market(s)

community services industry

Industry/Entity Type

Community Service

Requirements
Must have
• Specialist Provider of Multicultural Support Services
Nice to have
• "I acknowledge the traditional owners of the land on which we live, work and dream"
plus their flags as attached

```html
<!DOCTYPE html>
<html lang="en">
<head>
<meta charset="utf-8">
<title>Email Signatures – Darina Qubrosi</title>
<link rel="stylesheet" href="https://fonts.googleapis.com/css2?family=Arimo:ital,wght@0,400;0,700;1,400&display=swap">
<style>
  :root {
    --orange: #f7931e;
    --orange-deep: #d9730a;
    --orange-light: #f5ad55;
    --orange-pale: #fbd3a3;
    --charcoal: #333333;
    --white: #ffffff;
    --backdrop: #ebebeb;
  }
  * { margin: 0; padding: 0; box-sizing: border-box; }
  html, body { width: 1200px; height: 800px; overflow: hidden; }
  body {
    background: var(--backdrop);
    font-family: "Arimo", Arial, sans-serif;
    position: relative;
  }
  .signature {
    position: absolute;
    left: 217px;
    width: 766px;
    height: 261px;
    overflow: hidden;
    background: var(--white);
  }
  .signature--dark { top: 110px; }
  .signature--orange { top: 430px; }
  .signature__shapes { position: absolute; inset: 0; width: 766px; height: 261px; }

  .brand { position: absolute; text-align: center; width: 240px; }
  .brand__mark { display: block; margin: 0 auto; border-radius: 50%; background: var(--orange); }
  .brand__name {
    display: block;
    color: var(--orange);
    font-weight: 700;
    font-size: 23px;
    line-height: 1;
    letter-spacing: 1px;
    margin-top: 8px;
    white-space: nowrap;
  }
  .brand__tagline {
    display: block;
    color: var(--charcoal);
    font-size: 10px;
    line-height: 12px;
    letter-spacing: 0.6px;
    text-transform: uppercase;
    margin-top: 4px;
  }
  .signature--dark .brand { left: 27px; top: 42px; }
  .signature--dark .brand__mark { width: 84px; height: 84px; }
  .signature--orange .brand { left: 531px; top: 6px; }
  .signature--orange .brand__mark { width: 64px; height: 64px; }
  .signature--orange .brand__name { margin-top: 6px; }
  .signature--orange .brand__tagline { margin-top: 3px; }

  .social { position: absolute; display: flex; gap: 6px; }
  .social__item { width: 25px; height: 25px; border-radius: 3px; background: var(--orange); }
  .signature--dark .social { left: 87px; top: 215px; }
  .signature--dark .social__item { background: var(--charcoal); }
  .signature--orange .social { left: 634px; top: 185px; }

  .person { position: absolute; text-align: center; width: 360px; }
  .person__name { font-size: 27px; font-weight: 400; line-height: 1; }
  .person__role { font-size: 16px; font-style: italic; margin-top: 6px; }
  .signature--dark .person { left: 406px; top: 30px; }
  .signature--dark .person__name { color: var(--white); }
  .signature--dark .person__role { color: var(--orange); }
  .signature--orange .person { left: 97px; top: 30px; }
  .signature--orange .person__name { color: var(--white); }
  .signature--orange .person__role { color: var(--charcoal); }

  .contact { position: absolute; list-style: none; }
  .contact__row { position: absolute; left: 0; display: flex; align-items: center; white-space: nowrap; }
  .contact__icon { width: 22px; height: 22px; flex: none; }
  .contact__text {
    font-size: 14.5px;
    font-style: italic;
    line-height: 16px;
    color: var(--white);
    margin-left: 8px;
  }
  .signature--dark .contact { left: 463px; top: 0; }
  .signature--orange .contact { left: 153px; top: 0; }
  .contact__row--address { top: 94px; }
  .contact__row--tel { top: 133px; }
  .contact__row--mob { top: 161px; }
  .contact__row--mail { top: 189px; }
  .contact__row--web { top: 217px; }
  .icon-disc { fill: var(--orange); }
  .icon-glyph { fill: var(--charcoal); stroke: none; }
  .signature--orange .icon-disc { fill: var(--charcoal); }
  .signature--orange .icon-glyph { fill: var(--white); }
</style>
</head>
<body>

<section class="signature signature--dark">
  <svg class="signature__shapes" viewBox="0 0 766 261" aria-hidden="true">
    <polygon points="447,0 766,0 766,261 267,261" fill="var(--charcoal)"/>
    <polygon points="345,0 362,0 276,165 276,143" fill="var(--orange-pale)"/>
    <polygon points="362,0 385,0 292,170 292,140" fill="var(--orange-light)"/>
    <polygon points="392,0 418,0 296,245 250,245" fill="var(--orange-deep)"/>
    <polygon points="418,0 447,0 316,226 316,178" fill="var(--orange)"/>
  </svg>

  <div class="brand">
    <span class="brand__mark"></span>
    <span class="brand__name">MIVROTEL HAVEN</span>
    <span class="brand__tagline">Specialist Provider of<br>Multicultural Support Services</span>
  </div>
  <div class="social" aria-label="Social links">
    <span class="social__item"></span><span class="social__item"></span>
    <span class="social__item"></span><span class="social__item"></span>
  </div>

  <div class="person">
    <h1 class="person__name">Darina Qubrosi</h1>
    <p class="person__role">Support Coordinator</p>
  </div>

  <ul class="contact">
    <li class="contact__row contact__row--address">
      <svg class="contact__icon" viewBox="0 0 22 22"><circle class="icon-disc" cx="11" cy="11" r="11"/><path class="icon-glyph" d="M11 5a4 4 0 0 0-4 4c0 3 4 7 4 7s4-4 4-7a4 4 0 0 0-4-4zm0 5.5a1.5 1.5 0 1 1 0-3 1.5 1.5 0 0 1 0 3z"/></svg>
      <span class="contact__text">Unit 4, 517 Wattlebrook Lane,<br>Kemberly NSW 2893</span>
    </li>
    <li class="contact__row contact__row--tel">
      <svg class="contact__icon" viewBox="0 0 22 22"><circle class="icon-disc" cx="11" cy="11" r="11"/><path class="icon-glyph" d="M6 6h10v10H6z M8 8v6h6V8z M9 9h1.5l.7 1.6-.8.6a4 4 0 0 0 1.4 1.4l.6-.8L14 12.5V14c-3 0-5-2-5-5z"/></svg>
      <span class="contact__text">02 84427193</span>
    </li>
    <li class="contact__row contact__row--mob">
      <svg class="contact__icon" viewBox="0 0 22 22"><circle class="icon-disc" cx="11" cy="11" r="11"/><rect class="icon-glyph" x="7.5" y="5" width="7" height="12" rx="1.2"/></svg>
      <span class="contact__text">0427596314</span>
    </li>
    <li class="contact__row contact__row--mail">
      <svg class="contact__icon" viewBox="0 0 22 22"><circle class="icon-disc" cx="11" cy="11" r="11"/><path class="icon-glyph" d="M5.5 8.5 11 5l5.5 3.5V15h-11z"/><path d="M6.5 9.5 11 12l4.5-2.5" fill="none" stroke="var(--white)" stroke-width="1"/></svg>
      <span class="contact__text">darina.qu@mivrotelhaven.com</span>
    </li>
    <li class="contact__row contact__row--web">
      <svg class="contact__icon" viewBox="0 0 22 22"><circle class="icon-disc" cx="11" cy="11" r="11"/><circle class="icon-glyph" cx="11" cy="11" r="6"/><path d="M8 8.5c1.5 0 2 1 1.5 2s1 2.5 0 3.5M13 7c-.5 1.5 1 2 2 2.5" fill="none" stroke="var(--orange)" stroke-width="1.2"/></svg>
      <span class="contact__text">www.mivrotelhaven.com</span>
    </li>
  </ul>
</section>

<section class="signature signature--orange">
  <svg class="signature__shapes" viewBox="0 0 766 261" aria-hidden="true">
    <polygon points="0,0 430,0 663,261 0,261" fill="var(--orange)"/>
    <polygon points="549,132 766,132 766,261 663,261" fill="var(--charcoal)"/>
    <polygon points="0,112 134,261 0,261" fill="var(--charcoal)"/>
    <polygon points="0,146 103,261 0,261" fill="var(--white)"/>
  </svg>

  <div class="brand">
    <span class="brand__mark"></span>
    <span class="brand__name">MIVROTEL HAVEN</span>
    <span class="brand__tagline">Specialist Provider of<br>Multicultural Support Services</span>
  </div>
  <div class="social" aria-label="Social links">
    <span class="social__item"></span><span class="social__item"></span>
    <span class="social__item"></span><span class="social__item"></span>
  </div>

  <div class="person">
    <h2 class="person__name">Darina Qubrosi</h2>
    <p class="person__role">Support Coordinator</p>
  </div>

  <ul class="contact">
    <li class="contact__row contact__row--address">
      <svg class="contact__icon" viewBox="0 0 22 22"><circle class="icon-disc" cx="11" cy="11" r="11"/><path class="icon-glyph" d="M11 5a4 4 0 0 0-4 4c0 3 4 7 4 7s4-4 4-7a4 4 0 0 0-4-4zm0 5.5a1.5 1.5 0 1 1 0-3 1.5 1.5 0 0 1 0 3z"/></svg>
      <span class="contact__text">Unit 4, 517 Wattlebrook Lane,<br>Kemberly NSW 2893</span>
    </li>
    <li class="contact__row contact__row--tel">
      <svg class="contact__icon" viewBox="0 0 22 22"><circle class="icon-disc" cx="11" cy="11" r="11"/><path class="icon-glyph" d="M6 6h10v10H6z M8 8v6h6V8z M9 9h1.5l.7 1.6-.8.6a4 4 0 0 0 1.4 1.4l.6-.8L14 12.5V14c-3 0-5-2-5-5z"/></svg>
      <span class="contact__text">02 84427193</span>
    </li>
    <li class="contact__row contact__row--mob">
      <svg class="contact__icon" viewBox="0 0 22 22"><circle class="icon-disc" cx="11" cy="11" r="11"/><rect class="icon-glyph" x="7.5" y="5" width="7" height="12" rx="1.2"/></svg>
      <span class="contact__text">0427596314</span>
    </li>
    <li class="contact__row contact__row--mail">
      <svg class="contact__icon" viewBox="0 0 22 22"><circle class="icon-disc" cx="11" cy="11" r="11"/><path class="icon-glyph" d="M5.5 8.5 11 5l5.5 3.5V15h-11z"/><path d="M6.5 9.5 11 12l4.5-2.5" fill="none" stroke="var(--charcoal)" stroke-width="1"/></svg>
      <span class="contact__text">darina.qu@mivrotelhaven.com</span>
    </li>
    <li class="contact__row contact__row--web">
      <svg class="contact__icon" viewBox="0 0 22 22"><circle class="icon-disc" cx="11" cy="11" r="11"/><circle class="icon-glyph" cx="11" cy="11" r="6"/><path d="M8 8.5c1.5 0 2 1 1.5 2s1 2.5 0 3.5M13 7c-.5 1.5 1 2 2 2.5" fill="none" stroke="var(--charcoal)" stroke-width="1.2"/></svg>
      <span class="contact__text">www.mivrotelhaven.com</span>
    </li>
  </ul>
</section>

</body>
</html>
```